Place holder for book called SALT LANTERN WINTERS

I'm relying on your imaginative genius because I have no suggestions for you. Attached is a picture of the author when young if it will be of help. The only other info I can offer is that the author uses the alphabet as a theme.

Book info:
Title: SALT LANTERN WINTERS
Author: MARGOT KWELLAND

This is a memoir. It's a story of daring to hope when things seem hopeless, of problems when changing countries, of making success of dross. I'm looking for a design that is daring, eye-catching but promises hope. I hope it's not impossible.

Can you give me a place holder for the book to go onto my website and for pre-publicity? Then, in 6-9 months I'll pay another $150 for the completion of hardcover, paperback and ebook covers.

```html
<!DOCTYPE html>
<html lang="en">
<head>
<meta charset="utf-8">
<title>Salt Lantern Winters — Margot Kwelland</title>
<link rel="stylesheet" href="https://fonts.googleapis.com/css2?family=Montserrat:wght@600;700&family=Questrial&display=swap">
<style>
  :root {
    --stage: #2b2b2b;
    --cover-light: #ececec;
    --cover-mid: #dcdcdc;
    --ink: #3a3a3a;
    --sun-core: #f39a22;
    --sun-edge: #e2741a;
    --peak-dark: #5a5a5a;
    --peak-light: #bdbdbd;
  }
  * { margin: 0; padding: 0; box-sizing: border-box; }
  html, body {
    width: 1200px;
    height: 670px;
    overflow: hidden;
    background: var(--stage);
  }
  .canvas {
    position: relative;
    width: 1200px;
    height: 670px;
    background: var(--stage);
  }
  .cover {
    position: absolute;
    left: 383px;
    top: 15px;
    width: 433px;
    height: 640px;
    overflow: hidden;
    background:
      radial-gradient(ellipse at 40% 30%, var(--cover-light) 0%, var(--cover-mid) 100%);
    color: var(--ink);
    text-align: center;
  }
  .cover__author {
    position: absolute;
    top: 32px;
    left: 0;
    width: 100%;
    font-family: "Questrial", "Century Gothic", sans-serif;
    font-size: 21px;
    letter-spacing: 0.12em;
    font-weight: 400;
    color: #222;
  }
  .cover__sun {
    position: absolute;
    left: 156px;
    top: 165px;
    width: 104px;
    height: 104px;
    border-radius: 50%;
    background: radial-gradient(circle at 45% 45%, var(--sun-core) 0%, var(--sun-core) 55%, var(--sun-edge) 100%);
  }
  .cover__title {
    position: absolute;
    top: 208px;
    left: 0;
    width: 100%;
    font-family: "Montserrat", "Century Gothic", sans-serif;
    font-weight: 600;
    text-transform: uppercase;
  }
  .cover__title-small {
    display: block;
    font-size: 31px;
    line-height: 40px;
    letter-spacing: 0.02em;
  }
  .cover__title-large {
    display: block;
    font-size: 64px;
    line-height: 72px;
    letter-spacing: -0.01em;
  }
  .cover__peaks {
    position: absolute;
    left: 0;
    top: 420px;
    width: 100%;
    height: 150px;
    background: linear-gradient(180deg, rgba(189,189,189,0) 0%, var(--peak-light) 35%, var(--peak-dark) 70%, rgba(90,90,90,0) 100%);
    opacity: 0.75;
  }
</style>
</head>
<body>
  <main class="canvas">
    <section class="cover">
      <p class="cover__author">MARGOT KWELLAND</p>
      <div class="cover__sun" role="img" aria-label="Orange watercolour sun splash behind the title"></div>
      <h1 class="cover__title">
        <span class="cover__title-small">Salt</span>
        <span class="cover__title-large">Lantern</span>
        <span class="cover__title-large">Winters</span>
      </h1>
      <div class="cover__peaks" role="img" aria-label="Grey ink illustration of a mountain range"></div>
    </section>
  </main>
</body>
</html>
```